Business cards

Design business cards for our company. Just a straight, business like design with the logo, name, function and contact details

Target Market(s)

We are a innovative technological company active in water treatment

Industry/Entity Type

Water management

Contact Information for Business Card

Name, Function, email, telephone number, link to website

```html
<!DOCTYPE html>
<html lang="en">
<head>
<meta charset="utf-8">
<title>Marlin Tide Business Cards</title>
<link rel="stylesheet" href="https://fonts.googleapis.com/css2?family=Montserrat:wght@400;500;700&display=swap">
<style>
  :root {
    --bg: #ece9e4;
    --card: #ffffff;
    --blue: #2f97d8;
    --grey: #8f8f8f;
    --ink: #2b2b2b;
    --shadow: rgba(0, 0, 0, 0.14);
  }
  * { box-sizing: border-box; margin: 0; padding: 0; }
  html, body {
    width: 1200px;
    height: 834px;
    overflow: hidden;
    background: var(--bg);
    font-family: "Montserrat", sans-serif;
  }
  .sheet {
    width: 1200px;
    height: 834px;
    display: flex;
    align-items: center;
    justify-content: center;
    gap: 40px;
  }
  .card {
    width: 540px;
    height: 310px;
    background: var(--card);
    border-radius: 28px;
    box-shadow: 0 3px 0 #e2e2e2, 0 6px 0 #d8d8d8, 0 14px 30px var(--shadow);
    position: relative;
    overflow: hidden;
  }
  .brand {
    display: flex;
    align-items: center;
    gap: 12px;
    color: var(--blue);
    font-weight: 500;
    white-space: nowrap;
  }
  .brand-dot {
    border-radius: 50%;
    background: var(--blue);
    flex: none;
  }
  /* front */
  .card-front {
    display: flex;
    align-items: center;
    justify-content: center;
  }
  .card-front .brand { font-size: 50px; letter-spacing: 1px; }
  .card-front .brand-dot { width: 30px; height: 30px; }
  /* back */
  .card-back .brand {
    position: absolute;
    left: 30px;
    top: 132px;
    font-size: 27px;
  }
  .card-back .brand-dot { width: 18px; height: 18px; }
  .divider {
    position: absolute;
    left: 248px;
    top: 58px;
    width: 2px;
    height: 196px;
    background: var(--blue);
  }
  .contact {
    position: absolute;
    left: 272px;
    top: 62px;
    color: var(--ink);
  }
  .contact-name {
    color: var(--blue);
    font-weight: 700;
    font-size: 22px;
    letter-spacing: 1px;
    text-transform: uppercase;
  }
  .contact-role {
    color: var(--grey);
    font-size: 14px;
    margin-top: 3px;
    margin-bottom: 16px;
  }
  .contact-line {
    display: flex;
    align-items: center;
    gap: 9px;
    font-size: 14px;
    line-height: 24px;
  }
  .contact-line svg { width: 13px; height: 13px; fill: var(--blue); flex: none; }
  .contact-address {
    font-size: 14px;
    line-height: 21px;
    margin-top: 6px;
  }
</style>
</head>
<body>
<main class="sheet">
  <section class="card card-back" aria-label="Business card, contact side">
    <div class="brand"><span class="brand-dot"></span>Marlin Tide</div>
    <div class="divider"></div>
    <div class="contact">
      <p class="contact-name">Daniel Marsh</p>
      <p class="contact-role">Managing Director</p>
      <p class="contact-line">
        <svg viewBox="0 0 16 16" aria-hidden="true"><path d="M3.6 1.2l2.3 2.9-1.4 1.7a9 9 0 0 0 5.7 5.7l1.7-1.4 2.9 2.3-1.5 2.3C7.4 14.5 1.5 8.6 1.3 2.7z"/></svg>
        123 456 789
      </p>
      <p class="contact-line">
        <svg viewBox="0 0 16 16" aria-hidden="true"><path d="M1 3h14v1.2L8 9 1 4.2zM1 5.8l7 4.8 7-4.8V13H1z"/></svg>
        info@yourmail.com
      </p>
      <p class="contact-line">
        <svg viewBox="0 0 16 16" aria-hidden="true"><path d="M8 1a7 7 0 1 0 0 14A7 7 0 0 0 8 1zm0 1.5c.9 0 1.9 1.6 2.3 4.2H5.7C6.1 4.1 7.1 2.5 8 2.5zM5.6 8.2h4.8C10.2 11 9.1 13.5 8 13.5S5.8 11 5.6 8.2zM2.6 8.2h1.6c.1 1.9.5 3.5 1.2 4.6a5.5 5.5 0 0 1-2.8-4.6zm8.8 4.6c.7-1.1 1.1-2.7 1.2-4.6h1.6a5.5 5.5 0 0 1-2.8 4.6zM2.6 6.7a5.5 5.5 0 0 1 2.8-3.5c-.6 1-1 2.2-1.2 3.5zm9.2 0c-.2-1.3-.6-2.5-1.2-3.5a5.5 5.5 0 0 1 2.8 3.5z"/></svg>
        www.yourwebsite.com
      </p>
      <p class="contact-address">Your address, City<br>State, Zip 1234</p>
    </div>
  </section>

  <section class="card card-front" aria-label="Business card, brand side">
    <div class="brand"><span class="brand-dot"></span>Marlin Tide</div>
  </section>
</main>
</body>
</html>
```